Sandwich Board and Poster design promoting a medical aesthetic clinic

I am looking for a clean, modern and relaxing design promoting a medical physician-led aesthetic clinic.
Services offered are neuromodulator treatment (Quelvo) and Dermal Fillers.
Logo must be included.
Use the tag line "Refresh your look, revive your spirit."
Address is 204-205 27361 92 Ave, Surrey, V7K 2M4
604-555-0148
email - info@lumawellpine.ca
www.lumawellpine.ca

```html
<!DOCTYPE html>
<html lang="en">
<head>
<meta charset="utf-8">
<title>Lumawell Pine – Refresh Your Look</title>
<link href="https://fonts.googleapis.com/css2?family=Allura&family=Outfit:wght@300;400;600;700&family=Roboto+Condensed:wght@700&display=swap" rel="stylesheet">
<style>
  :root {
    --navy: #1f3d5c;
    --gold: #d2ab33;
    --gold-light: #ecd58c;
    --cream: #fbf1d4;
    --cream-top: #fdf8ec;
    --white: #ffffff;
  }
  * { margin: 0; padding: 0; box-sizing: border-box; }
  html, body { width: 720px; height: 1200px; overflow: hidden; background: var(--white); }
  .poster {
    position: relative;
    width: 720px;
    height: 1200px;
    overflow: hidden;
    background: linear-gradient(180deg, var(--cream-top) 0%, #fbf3dc 55%, var(--cream) 100%);
    font-family: "Outfit", sans-serif;
    color: var(--navy);
  }
  .hero-photo {
    position: absolute;
    left: 0; top: 0;
    width: 720px; height: 700px;
    background:
      radial-gradient(ellipse 38% 44% at 45% 42%, #f0d3bf 0%, #ecd0bc 55%, rgba(240,215,195,0) 100%),
      radial-gradient(ellipse 22% 26% at 88% 22%, #8fc9ec 0%, rgba(143,201,236,0) 100%),
      radial-gradient(ellipse 16% 22% at 84% 72%, #9bd0ef 0%, rgba(155,208,239,0) 100%),
      linear-gradient(180deg, #f6f2ef 0%, #f7efe4 70%, rgba(251,243,220,0) 100%);
  }
  .script-title {
    position: absolute;
    left: 60px; top: 590px;
    font-family: "Allura", cursive;
    font-size: 118px;
    line-height: 1;
    white-space: nowrap;
    color: var(--navy);
  }
  .headline {
    position: absolute;
    right: 62px;
    line-height: 1;
    white-space: nowrap;
    text-align: right;
    text-transform: uppercase;
  }
  .headline-look { top: 740px; font-size: 76px; font-weight: 700; letter-spacing: -1px; }
  .headline-spirit { top: 822px; font-size: 55px; font-weight: 700; letter-spacing: -0.8px; }
  .headline-spirit .light { font-weight: 300; }
  .rule {
    position: absolute;
    left: 60px; top: 888px;
    width: 598px; height: 1.5px;
    background: var(--gold);
  }
  .services {
    position: absolute;
    left: 60px; top: 904px;
    list-style: none;
    font-size: 21px;
    font-weight: 400;
    text-transform: uppercase;
    white-space: nowrap;
  }
  .services li { display: flex; align-items: center; gap: 9px; height: 33px; }
  .tick { width: 21px; height: 21px; flex: none; }
  .brand-name {
    position: absolute;
    left: 400px; top: 1040px;
    display: flex; align-items: center; gap: 10px;
    font-size: 22px;
    font-weight: 400;
    letter-spacing: 5px;
    white-space: nowrap;
    text-transform: uppercase;
    color: var(--navy);
  }
  .brand-dot { width: 14px; height: 14px; border-radius: 50%; background: var(--navy); }
  .footer-wave { position: absolute; left: 0; top: 0; width: 720px; height: 1200px; }
  .phone {
    position: absolute;
    left: 62px; top: 1079px;
    display: flex; align-items: center; gap: 10px;
    font-family: "Roboto Condensed", sans-serif;
    font-weight: 700;
    font-size: 44px;
    white-space: nowrap;
    color: var(--navy);
  }
  .phone-icon { width: 52px; height: 52px; }
  .contacts {
    position: absolute;
    left: 78px; top: 1145px;
    display: flex; gap: 18px;
    font-size: 11px;
    font-weight: 400;
    text-transform: uppercase;
    color: var(--navy);
  }
  .contacts span { display: flex; align-items: center; gap: 6px; white-space: nowrap; }
  .contacts svg { width: 22px; height: 22px; flex: none; }
</style>
</head>
<body>
<main class="poster">
  <div class="hero-photo" role="img" aria-label="Photo of a woman with closed eyes receiving a forehead injection from gloved hands, with a small white flower"></div>

  <svg class="footer-wave" viewBox="0 0 720 1200" aria-hidden="true">
    <path d="M0,1032 C130,992 310,1004 470,1094 C565,1140 660,1066 720,994" fill="none" stroke="var(--gold-light)" stroke-width="10"/>
    <path d="M0,1046 C125,1008 305,1020 470,1108 C565,1154 660,1082 720,1008 L720,1200 L0,1200 Z" fill="var(--white)"/>
    <path d="M0,1052 C125,1014 305,1026 470,1114 C565,1160 660,1088 720,1014 L720,1200 L0,1200 Z" fill="var(--gold)"/>
  </svg>

  <div class="script-title">Refresh</div>
  <div class="headline headline-look">Your Look</div>
  <div class="headline headline-spirit"><span class="light">Revive</span> Your Spirit.</div>
  <div class="rule"></div>

  <ul class="services">
    <li><svg class="tick" viewBox="0 0 20 20"><circle cx="10" cy="10" r="10" fill="var(--gold)"/><path d="M5.5 10.2l3 3 6-6" fill="none" stroke="var(--white)" stroke-width="1.8" stroke-linecap="round" stroke-linejoin="round"/></svg>Neuromodulator Treatment (Quelvo)</li>
    <li><svg class="tick" viewBox="0 0 20 20"><circle cx="10" cy="10" r="10" fill="var(--gold)"/><path d="M5.5 10.2l3 3 6-6" fill="none" stroke="var(--white)" stroke-width="1.8" stroke-linecap="round" stroke-linejoin="round"/></svg>Dermal Fillers</li>
  </ul>

  <div class="brand-name"><span class="brand-dot"></span>Lumawell Pine</div>

  <div class="phone">
    <svg class="phone-icon" viewBox="0 0 52 52" aria-hidden="true">
      <circle cx="26" cy="26" r="25" fill="var(--cream)"/>
      <circle cx="26" cy="26" r="20" fill="none" stroke="var(--gold)" stroke-width="2"/>
      <path d="M19 16c1-1 2.4-1 3.2 0l2.6 3.4c.6.8.5 1.9-.2 2.6l-1.6 1.6c1.2 2.6 3.2 4.6 5.8 5.8l1.6-1.6c.7-.7 1.8-.8 2.6-.2l3.4 2.6c1 .8 1 2.2 0 3.2l-1.6 1.6c-1.6 1.6-4.2 1.800-6.2.6-4.8-2.8-8.6-6.6-11.4-11.4-1.2-2-1-4.6.6-6.2z" fill="var(--navy)"/>
      <path d="M30 17a7 7 0 0 1 5 5M30 13a11 11 0 0 1 9 9" fill="none" stroke="var(--navy)" stroke-width="1.8" stroke-linecap="round"/>
    </svg>
    604-555-0148
  </div>

  <div class="contacts">
    <span><svg viewBox="0 0 22 22"><circle cx="11" cy="11" r="11" fill="var(--cream)"/><path d="M11 5a4 4 0 0 0-4 4c0 3 4 7.5 4 7.5s4-4.5 4-7.5a4 4 0 0 0-4-4z" fill="var(--navy)"/><circle cx="11" cy="9" r="1.5" fill="var(--cream)"/></svg>204-205 27361 92 Ave, Surrey, V7K 2M4</span>
    <span><svg viewBox="0 0 22 22"><circle cx="11" cy="11" r="11" fill="var(--navy)"/><rect x="6" y="7.5" width="10" height="7" rx="1" fill="var(--cream)"/><path d="M6.5 8l4.5 3.5L15.5 8" fill="none" stroke="var(--navy)" stroke-width="1"/></svg>info@lumawellpine.ca</span>
    <span><svg viewBox="0 0 22 22"><circle cx="11" cy="11" r="11" fill="var(--cream)"/><circle cx="11" cy="11" r="5.5" fill="none" stroke="var(--navy)" stroke-width="1.2"/><path d="M5.5 11h11M11 5.5c-2.5 3-2.5 8 0 11M11 5.5c2.5 3 2.5 8 0 11" fill="none" stroke="var(--navy)" stroke-width="1"/></svg>www.lumawellpine.ca</span>
  </div>
</main>
</body>
</html>
```